Cover for Where the Quiet River Bends Beyond Our Morning

Cover for a book that describes everything that happens to a person, from pre-birth life plans through growing in compassion and wisdom to death and living in the afterlife. The information is revealed in messages from people living in the life after this life. The title is Lanterns Along the Hidden Stair of Every Soul: Gathered from Voices Dwelling in the Further Meadow. Author is T. Morven Ashdale. Book size is 6 by 9.

Target Market(s)

General

Font styles to use
Serif

```html
<!DOCTYPE html>
<html lang="en">
<head>
<meta charset="utf-8">
<title>Lanterns Along the Hidden Stair of Every Soul — Cover</title>
<link rel="stylesheet" href="https://fonts.googleapis.com/css2?family=Bodoni+Moda:wght@500&family=Josefin+Sans:wght@400;600;700&display=swap">
<style>
  :root {
    --backdrop: #a2a2a2;
    --paper: #ffffff;
    --title-red: #d8000f;
    --ink: #1f1f1f;
    --band-text: #ffffff;
    --mist-light: #fbfcfd;
    --mist-mid: #dfe5ec;
    --mist-deep: #b9c3cf;
  }
  * { box-sizing: border-box; margin: 0; padding: 0; }
  html, body {
    width: 687px; height: 1200px; overflow: hidden;
    background: var(--backdrop);
  }
  .cover {
    position: absolute; left: 43px; top: 150px;
    width: 600px; height: 900px;
    background: var(--paper);
    box-shadow: 4px 6px 14px rgba(0,0,0,0.35);
    overflow: hidden;
  }
  .cover-art {
    position: absolute; left: 0; top: 85px;
    width: 600px; height: 730px;
    background:
      radial-gradient(ellipse 28% 55% at 50% 52%, var(--mist-light) 0%, rgba(251,252,253,0.9) 45%, rgba(251,252,253,0) 100%),
      linear-gradient(90deg, var(--mist-deep) 0%, var(--mist-mid) 22%, var(--mist-light) 45%, var(--mist-light) 55%, var(--mist-mid) 78%, var(--mist-deep) 100%);
  }
  .cover-art::after {
    content: ""; position: absolute; inset: 0;
    background: linear-gradient(180deg, rgba(255,255,255,0.6) 0%, rgba(255,255,255,0) 10%, rgba(255,255,255,0) 82%, var(--paper) 100%);
  }
  .title {
    position: absolute; left: 68px; top: 80px; width: 463px;
    font-weight: normal;
  }
  .title-main {
    display: block; width: 463px;
    font-family: "Bodoni Moda", serif; font-weight: 500;
    font-size: 84px; line-height: 96px; letter-spacing: -2px;
    color: var(--title-red); text-align: center; white-space: nowrap;
  }
  .title-row {
    display: flex; justify-content: space-between; align-items: center;
    width: 463px; height: 88px;
  }
  .title-lines {
    display: block;
    font-family: "Josefin Sans", sans-serif; font-weight: 400;
    font-size: 34px; line-height: 42px; color: var(--ink);
    letter-spacing: -0.5px; white-space: nowrap;
  }
  .title-accent {
    display: block;
    font-family: "Josefin Sans", sans-serif; font-weight: 700;
    font-size: 80px; line-height: 88px; color: var(--ink);
    letter-spacing: -1px; padding-top: 12px; white-space: nowrap;
  }
  .title-band {
    display: block; width: 463px; height: 46px; margin-top: 6px;
    background: var(--ink); color: var(--band-text);
    font-family: "Josefin Sans", sans-serif; font-weight: 600;
    font-size: 28px; line-height: 52px; text-align: center;
    letter-spacing: 1px;
  }
  .credit {
    position: absolute; left: 0; top: 780px; width: 600px;
    text-align: center; font-family: "Josefin Sans", sans-serif;
  }
  .credit-lead {
    color: var(--title-red); font-weight: 600;
    font-size: 19px; letter-spacing: 0.5px; line-height: 22px;
  }
  .credit-source {
    color: var(--ink); font-weight: 400;
    font-size: 13px; letter-spacing: 4px; line-height: 22px;
  }
</style>
</head>
<body>
  <main class="cover">
    <div class="cover-art" role="img" aria-label="Misty white colonnade of tall classical columns with a lone figure walking toward a bright light"></div>
    <h1 class="title">
      <span class="title-main">LANTERNS</span>
      <span class="title-row">
        <span class="title-lines">ALONG THE<br>HIDDEN</span>
        <span class="title-accent">STAIR</span>
      </span>
      <span class="title-band">OF EVERY SOUL</span>
    </h1>
    <p class="credit">
      <span class="credit-lead">GATHERED FROM</span><br>
      <span class="credit-source">VOICES DWELLING IN THE FURTHER MEADOW</span>
    </p>
  </main>
</body>
</html>
```